Information Technology Company needs a Website...

We need a single page website for new technology company called:

MERIVALE CREST TECHNOLOGY GROUP
Based in Ojai CA.

We are offering three primary services:

- Business Solutions

- IT Services

- Software Implementation and Consulting

We want a single page design where all content scrolls down/up on one page. We're looking for the following characteristics:

- Home/Landing
- Active background with panoramic view (Will provide content)

- Business Solutions, IT Services, Software Implementation and Consulting

List of software vendors we recommend (Company logos)

- About
- History
- Our Team
- Partners

I'll upload our new logo as soon as we get the design files. I'll also send over some example website layout's that we like shortly.

Target Market(s)

Small/Medium Businesses

Industry/Entity Type

Information Technology

Number of Pages Required

1 page

Font styles to use
Other font styles liked:
• Sansation

Requirements
Must have
• Full page browser width, easy navigation and visibility. Creative design, not like every other "Technology" website template. Should be the "One Page" design where each section is below the next and the user scrolls down the page through the whole site. I like the concept of the following website in the main "Whiteboard" image:
• http://www.plinkoria-sample.com/design/4082913
• And the way this site does the active panoramic background:
• http://www.vantrelwork-sample.com/
• Something interesting and appealing to potential clients looking for Small/Medium business solutions and IT Services.
• Use uploaded Logo to establish color and theme for website.
Should not have
• Look the same as every other information technology website template.

```html
<!DOCTYPE html>
<html lang="en">
<head>
<meta charset="utf-8">
<title>Merivale Crest Technology Group</title>
<link href="https://fonts.googleapis.com/css2?family=Montserrat:wght@400;500;600;700&family=Play:wght@400;700&display=swap" rel="stylesheet">
<style>
:root{
  --orange:#f26a3e;
  --btn-top:#f39233;
  --btn-bottom:#e2711c;
  --ink:#333333;
  --ink-soft:#444444;
  --band:#ebebeb;
  --white:#ffffff;
  --footer:#f26a44;
}
*{margin:0;padding:0;box-sizing:border-box}
html,body{width:1200px;height:2707px;overflow:hidden;background:var(--white)}
body{position:relative;font-family:"Montserrat",Arial,sans-serif;color:var(--ink)}
.abs{position:absolute}
.heading{font-family:"Play","Montserrat",sans-serif;font-weight:700}

/* header */
.brand{left:141px;top:22px;width:240px}
.brand-mark{display:block;width:20px;height:20px;border:3px solid var(--orange);margin-bottom:4px}
.brand-name{font-family:"Montserrat",sans-serif;font-weight:600;font-size:15px;color:var(--ink-soft);line-height:1.15;letter-spacing:.5px;white-space:nowrap}
.nav{top:48px;left:523px;font-size:16px;font-weight:500;color:var(--ink-soft)}
.nav span{position:absolute;white-space:nowrap}
.nav .active{color:var(--orange)}

/* hero */
.hero{left:51px;top:108px;width:1099px;height:423px;background:linear-gradient(100deg,#4a4d50 0%,#5c5f62 45%,#3b3d40 100%)}
.hero-title{left:166px;top:196px;font-size:44px;color:var(--orange)}
.hero-sub{left:166px;top:248px;font-size:30px;color:var(--white);font-family:"Montserrat",sans-serif;font-weight:600}
.hero-text{left:166px;top:298px;width:290px;font-size:13px;font-weight:700;color:var(--white);line-height:1.4}
.hero-arrow{width:36px;height:36px;border-radius:50%;background:rgba(200,210,220,.55)}
.dots{left:548px;top:498px;display:flex;gap:12px}
.dots i{width:14px;height:14px;border-radius:50%;background:var(--white);display:block}

/* welcome */
.welcome-band{left:51px;top:531px;width:1099px;height:153px;background:var(--band)}
.welcome-title{left:141px;top:556px;font-size:33px;color:var(--ink)}
.welcome-title b{color:var(--orange)}
.welcome-text{left:141px;top:607px;width:700px;font-size:11.6px;line-height:1.55;color:var(--ink)}
.btn{display:flex;align-items:center;justify-content:center;color:var(--white);font-size:14px;font-weight:600;background:linear-gradient(var(--btn-top),var(--btn-bottom));border-radius:3px}

/* sections */
.section-title{left:0;width:1200px;text-align:center;font-size:33px;color:var(--ink)}
.section-lead{left:180px;width:840px;text-align:center;font-size:12.5px;line-height:1.55;color:var(--ink)}
.service{width:260px;text-align:center}
.service .ring{width:124px;height:124px;margin:0 auto;border-radius:50%;border:3px solid var(--orange);display:flex;align-items:center;justify-content:center}
.service h3{margin-top:40px;font-size:14.5px;font-weight:700;color:var(--ink)}
.service p{margin:16px auto 0;width:200px;font-size:13px;line-height:1.5}

.history-photo{left:51px;top:1191px;width:453px;height:318px;background:linear-gradient(90deg,#556069 0%,#7d868d 55%,#d9d6d2 100%)}
.history-panel{left:504px;top:1191px;width:646px;height:318px;background:var(--band)}
.history-title{left:538px;top:1214px;font-size:35px;color:var(--orange)}
.history-text{left:541px;top:1272px;width:420px;font-size:13px;line-height:1.75}

.member{width:300px;text-align:center}
.member .photo{width:202px;height:202px;border-radius:50%;margin:0 auto}
.member h4{margin-top:34px;font-size:21px;font-weight:600;color:var(--orange)}
.member .role{margin-top:4px;font-size:16px}
.member p{margin:26px auto 0;width:260px;font-size:14px;line-height:1.4}

.partners{left:51px;top:2114px;width:1099px;height:267px;background:var(--band)}
.partners-title{left:0;top:2140px;width:1200px;text-align:center;font-size:33px;color:var(--orange)}
.badge{top:2224px;width:244px;height:108px;border:4px solid #dedede;background:#f6f6f6}
.badge i{position:absolute;left:50%;top:50%;width:120px;height:30px;margin:-15px 0 0 -60px;background:#e0e0e0;border-radius:3px}

.footer{left:51px;top:2381px;width:1099px;height:326px;background:var(--footer);color:var(--white)}
.foot-head{font-size:15px;font-weight:700;color:var(--white)}
.foot-line{font-size:16px;color:var(--white)}
.social{top:2475px;width:51px;height:51px;border:2px solid var(--white);display:flex;align-items:center;justify-content:center;font-size:12px;font-weight:600;color:var(--white)}
.rule{left:141px;top:2626px;width:920px;height:1px;background:rgba(255,255,255,.45)}
</style>
</head>
<body>

<header>
  <div class="abs brand"><span class="brand-mark"></span><div class="brand-name">MERIVALE CREST<br>TECHNOLOGY GROUP</div></div>
  <nav class="abs nav">
    <span class="active" style="left:0">HOME</span>
    <span style="left:87px">ABOUT US</span>
    <span style="left:208px">HISTORY</span>
    <span style="left:314px">OUR TEAM</span>
    <span style="left:443px">PARTNERS</span>
  </nav>
</header>

<section>
  <div class="abs hero" role="img" aria-label="Businessman in a suit facing a chalkboard covered with business strategy sketches"></div>
  <h1 class="abs heading hero-title">Merivale Crest</h1>
  <div class="abs hero-sub">TECHNOLOGY GROUP</div>
  <p class="abs hero-text">Lorem ipsum dolor sit amet, consectetur adipiscing elit, sed do eiusmod tempor incididunt ut labore et dolore magna aliqua.</p>
  <div class="abs hero-arrow" style="left:101px;top:330px"><svg width="36" height="36"><path d="M20 11 L13 18 L20 25" fill="none" stroke="#fff" stroke-width="2.5"/></svg></div>
  <div class="abs hero-arrow" style="left:1060px;top:330px"><svg width="36" height="36"><path d="M16 11 L23 18 L16 25" fill="none" stroke="#fff" stroke-width="2.5"/></svg></div>
  <div class="abs dots"><i></i><i></i><i></i><i></i></div>
</section>

<section>
  <div class="abs welcome-band"></div>
  <h2 class="abs heading welcome-title">Welcome to <b>Merivale Crest</b></h2>
  <p class="abs welcome-text">Lorem ipsum dolor sit amet, consectetur adipiscing elit, sed do eiusmod tempor incididunt ut labore et dolore magna aliqua. Ut enim ad minim veniam, quis nostrud exercitation ullamco laboris nisi ut aliquip ex ea commodo consequat. Duis aute irure dolor in reprehenderit in voluptate velit esse cillum dolore eu fugiat nulla pariatur.</p>
  <div class="abs btn" style="left:917px;top:590px;width:142px;height:45px">More Info</div>
</section>

<section>
  <h2 class="abs heading section-title" style="top:725px">Our Services</h2>
  <p class="abs section-lead" style="top:788px">Lorem ipsum dolor sit amet, consectetur adipiscing elit, sed do eiusmod tempor incididunt ut labore et dolore magna aliqua. Ut enim ad minim veniam, quis nostrud exercitation ullamco laboris nisi ut aliquip ex ea commodo consequat.</p>

  <div class="abs service" style="left:186px;top:882px">
    <div class="ring"><svg width="56" height="56" viewBox="0 0 56 56"><rect x="6" y="18" width="44" height="30" rx="3" fill="var(--orange)"/><rect x="20" y="10" width="16" height="10" rx="2" fill="none" stroke="var(--orange)" stroke-width="4"/></svg></div>
    <h3>BUSINESS SOLUTIONS</h3>
    <p>Lorem ipsum dolor sit amet, consectetur adipiscing elit, sed do eiusmod</p>
  </div>
  <div class="abs service" style="left:457px;top:882px">
    <div class="ring"><svg width="56" height="56" viewBox="0 0 56 56"><rect x="6" y="8" width="44" height="30" rx="2" fill="none" stroke="var(--orange)" stroke-width="4"/><rect x="24" y="38" width="8" height="8" fill="var(--orange)"/><rect x="14" y="46" width="28" height="4" fill="var(--orange)"/></svg></div>
    <h3>IT SERVICES</h3>
    <p>Lorem ipsum dolor sit amet, consectetur adipiscing elit, sed do eiusmod</p>
  </div>
  <div class="abs service" style="left:731px;top:882px">
    <div class="ring"><svg width="56" height="56" viewBox="0 0 56 56"><circle cx="28" cy="28" r="18" fill="none" stroke="var(--orange)" stroke-width="8" stroke-dasharray="7 7"/><circle cx="28" cy="28" r="14" fill="var(--orange)"/><circle cx="28" cy="28" r="6" fill="#fff"/></svg></div>
    <h3>SOFTWARE IMPLEMENTATION</h3>
    <p>Lorem ipsum dolor sit amet, consectetur adipiscing elit, sed do eiusmod</p>
  </div>
</section>

<section>
  <div class="abs history-photo" role="img" aria-label="Woman drawing a network diagram with internet, firewall and server on a glass board"></div>
  <div class="abs history-panel"></div>
  <h2 class="abs heading history-title">History</h2>
  <div class="abs history-text">
    <p>Lorem ipsum dolor sit amet, consectetur adipiscing elit, sed do eiusmod tempor incididunt ut labore et dolore magna aliqua. Ut enim ad minim veniam, quis nostrud exercitation.</p>
    <p style="margin-top:16px">Excepteur sint occaecat cupidatat non proident, sunt in culpa qui officia deserunt mollit anim id est laborum.</p>
  </div>
  <div class="abs btn" style="left:541px;top:1435px;width:139px;height:43px">Know More</div>
</section>

<section>
  <h2 class="abs heading section-title" style="top:1546px">Meet Our Team</h2>
  <p class="abs section-lead" style="top:1607px;left:290px;width:620px">Lorem ipsum dolor sit amet, consectetur adipiscing elit, sed do eiusmod tempor incididunt ut labore et dolore magna aliqua.</p>

  <div class="abs member" style="left:94px;top:1686px">
    <div class="photo" role="img" aria-label="Portrait of team member Corwin Hale" style="background:radial-gradient(circle at 50% 45%,#c9a48a 0%,#6e5a3c 60%,#3f4a2c 100%)"></div>
    <h4>Corwin Hale</h4><div class="role">Developer</div>
    <p>Excepteur sint occaecat cupidatat non proident, sunt in culpa qui officia .</p>
  </div>
  <div class="abs member" style="left:447px;top:1686px">
    <div class="photo" role="img" aria-label="Portrait of team member Tavis Renner" style="background:radial-gradient(circle at 50% 45%,#d8a88a 0%,#7f6a3a 60%,#4d5a2a 100%)"></div>
    <h4>Tavis Renner</h4><div class="role">Developer</div>
    <p>Excepteur sint occaecat cupidatat non proident, sunt in culpa qui officia .</p>
  </div>
  <div class="abs member" style="left:807px;top:1686px">
    <div class="photo" role="img" aria-label="Black and white portrait of team member Elden Marsh" style="background:radial-gradient(circle at 50% 45%,#d4d4d4 0%,#9a9a9a 60%,#5a5a5a 100%)"></div>
    <h4>Elden Marsh</h4><div class="role">Developer</div>
    <p>Excepteur sint occaecat cupidatat non proident, sunt in culpa qui officia .</p>
  </div>
</section>

<section>
  <div class="abs partners"></div>
  <h2 class="abs heading partners-title">Our Partners</h2>
  <svg class="abs" style="left:88px;top:2262px" width="22" height="40"><path d="M18 4 L6 20 L18 36" fill="none" stroke="#d6d6d6" stroke-width="3"/></svg>
  <svg class="abs" style="left:1090px;top:2262px" width="22" height="40"><path d="M4 4 L16 20 L4 36" fill="none" stroke="#d6d6d6" stroke-width="3"/></svg>
  <div class="abs badge" style="left:144px"><i></i></div>
  <div class="abs badge" style="left:480px"><i></i></div>
  <div class="abs badge" style="left:814px"><i></i></div>
</section>

<footer>
  <div class="abs footer"></div>
  <div class="abs foot-head" style="left:143px;top:2426px">CONTACT US</div>
  <div class="abs foot-line" style="left:143px;top:2467px">418 Orlen Lane, Vessa Ridge, CA 93027</div>
  <div class="abs foot-line" style="left:143px;top:2505px">P: 1.555.0142.730</div>
  <div class="abs foot-line" style="left:143px;top:2543px">E: hello@merivalecrest-sample.com</div>
  <div class="abs foot-head" style="left:729px;top:2426px">FOLLOW US ON</div>
  <div class="abs social" style="left:729px">Nook</div>
  <div class="abs social" style="left:807px">Wave</div>
  <div class="abs social" style="left:884px"><svg width="24" height="24" viewBox="0 0 24 24"><circle cx="5" cy="19" r="2.6" fill="#fff"/><path d="M3 11a10 10 0 0 1 10 10" fill="none" stroke="#fff" stroke-width="3"/><path d="M3 4a17 17 0 0 1 17 17" fill="none" stroke="#fff" stroke-width="3"/></svg></div>
  <div class="abs social" style="left:962px">Link</div>
  <div class="abs rule"></div>
  <div class="abs foot-line" style="left:141px;top:2650px">Home \ About Us \ History \ Our Team \ Partners</div>
  <div class="abs foot-line" style="left:729px;top:2650px">Copyright © 2016. All Rights Reserved</div>
</footer>

</body>
</html>
```